Fun, Colorful, Classy ,& Stylish Wine Bacholorette Labels

Thanks For Stopping By, My Hope is That we Can Knock this out of The Park :)
Ok, So Here is Our Big Idea.

We are going to be launching another product on brellix that are similar to these below.
https://www.brellix.com/Bottle-Labels-Engagement-Party-Bachelorette/item/Q72KXN48TZ/ref=sr_1_8?s=home-garden&ie=UTF8&qid=1498201157&sr=1-8&keywords=bridal+wine+labels&imgID=73qa2WDZpLm&preST=SY300_QL70&imgSrc=srch
https://www.brellix.com/Pop-The-Bubbly-Lovebirds-Engagement/item/Q58WMR31VD/ref=pd_sim_79_3?_encoding=UTF8&pd_rd_i=Q58WMR31VD&pd_rd_r=LKPZW47D2MX93Q08F61B&pd_rd_w=tcV4q&pd_rd_wg=n9JeK&psc=1&refRID=LKPZW47D2MX93Q08F61B
https://www.brellix.com/Bachelorette-Wedding-Wine-Bottle-Labels/item/Q94HTY26LB/ref=pd_sim_79_2?_encoding=UTF8&pd_rd_i=Q94HTY26LB&pd_rd_r=LKPZW47D2MX93Q08F61B&pd_rd_w=tcV4q&pd_rd_wg=n9JeK&psc=1&refRID=LKPZW47D2MX93Q08F61B

We are going to do a few Styles.
1 Bachelorette , Engagement Party - Bridal Gift - Funny - 6Pc

We are planning to do a few more but let’s start with this one first.

size: 4'' x 5'' - mock up should also be done on the bottle. pick from one of the quotes below and design a label that will knock our socks off. :)

the wine bottle pics are just an example of another company that have done something similar.

Industry/Entity Type

Wedding

Font styles to use
Script

Colors
e667a6
ffffff
33a6d7
b768aa
e34197
fbee3d
abd036
33b8a4
6b449b

Requirements
Must have
• Colorful Humor and tasteful
Nice to have
• a creative spin on concept
Should not have
• should not be plain jane/ boring.

```html
<!DOCTYPE html>
<html lang="en">
<head>
<meta charset="utf-8">
<title>Engagement Wine Labels – Set of 6</title>
<link rel="stylesheet" href="https://fonts.googleapis.com/css2?family=Kaushan+Script&family=Great+Vibes&family=Montserrat:wght@300;400&display=swap">
<style>
  :root {
    --ink: #1f1f1f;
    --paper: #ffffff;
    --gold: #c9a24a;
    --gold-light: #ecd79a;
    --gold-deep: #a87f2c;
    --blush: #f6dcd8;
    --blush-soft: #fbeeed;
    --charcoal: #262b2a;
    --pink-confetti: #f0c9c4;
  }
  * { box-sizing: border-box; margin: 0; padding: 0; }
  html, body { width: 1200px; height: 945px; overflow: hidden; background: var(--paper); }
  .label-set {
    width: 1200px; height: 945px;
    display: flex; align-items: center; justify-content: center; gap: 20px;
  }
  .label {
    position: relative; width: 176px; height: 220px; overflow: hidden;
    background: var(--paper); color: var(--ink);
    box-shadow: 0 0 0 1px #eee;
    font-family: "Montserrat", sans-serif;
  }
  .abs { position: absolute; }
  .script-brush { font-family: "Kaushan Script", cursive; }
  .script-fine { font-family: "Great Vibes", cursive; }
  .caps { font-weight: 300; text-transform: uppercase; letter-spacing: 0.02em; }

  /* 1 */
  .label--real { background: linear-gradient(160deg, #fbf6ea, var(--gold-light) 45%, #fbf6ea 70%, #e9d190); }
  .label--real .badge {
    left: 14px; top: 40px; width: 148px; height: 148px; border-radius: 50%;
    background: var(--paper); box-shadow: 0 2px 6px rgba(0,0,0,.15);
  }
  .label--real .word-shit { left: 20px; top: 52px; font-size: 48px; line-height: 1; }
  .label--real .word-got { left: 24px; top: 108px; font-size: 20px; }
  .label--real .ring-art { left: 40px; top: 140px; width: 20px; height: 24px; border-radius: 50% 50% 50% 50%; background: linear-gradient(#ddd, #888); }
  .label--real .word-real { left: 64px; top: 128px; font-size: 38px; line-height: 1; }

  /* 2 */
  .label--yeah { background: var(--blush-soft); }
  .label--yeah .heart { left: 30px; top: 18px; width: 116px; height: 104px; }
  .label--yeah .word-yeah { left: 0; right: 0; top: 122px; text-align: center; font-size: 32px; }
  .label--yeah .tagline { left: 0; right: 0; top: 166px; text-align: center; font-size: 11px; }

  /* 3 */
  .label--holy { background: var(--blush); }
  .label--holy .word-holy { left: 44px; top: 6px; font-size: 36px; line-height: 0.8; }
  .label--holy .hearts-art { left: 0; top: 62px; width: 176px; height: 64px;
    background: linear-gradient(90deg, var(--gold-light), #fff 40%, #d9b86a 70%, #3a3a3a); }
  .label--holy .gold-band { left: 0; top: 126px; width: 176px; height: 16px;
    background: linear-gradient(90deg, var(--gold-deep), var(--gold-light), var(--gold)); }
  .label--holy .dark-band { left: 0; top: 142px; width: 176px; height: 78px; background: var(--charcoal); color: var(--paper);
    display: flex; align-items: center; justify-content: center; text-align: center; font-size: 13px; line-height: 1.5; }

  /* 4 */
  .label--mrs {
    background: repeating-linear-gradient(180deg, var(--charcoal) 0 9px, var(--paper) 9px 11px, var(--gold) 11px 17px, var(--paper) 17px 19px);
  }
  .label--mrs .heart { left: 4px; top: 44px; width: 168px; height: 150px; }
  .label--mrs .word-mrs { left: 0; right: 0; top: 86px; text-align: center; font-size: 40px; }

  /* 5 */
  .label--finally .confetti { left: 0; width: 176px; height: 30px;
    background: linear-gradient(90deg, var(--pink-confetti), var(--gold-light), var(--charcoal) 140%); opacity: .55; }
  .label--finally .confetti--top { top: 0; }
  .label--finally .confetti--bottom { bottom: 0; }
  .label--finally .hand-art { left: 60px; top: 38px; width: 56px; height: 66px; border-radius: 10px;
    background: linear-gradient(#f3f3f3, #d8d8d8); }
  .label--finally .word-finally { left: 0; right: 0; top: 106px; text-align: center; font-size: 36px; line-height: 0.9; }

  /* 6 */
  .label--omg { background: linear-gradient(180deg, #b7903c, var(--gold-light) 30%, #fff3cf 50%, var(--gold-light) 70%, #b7903c); }
  .label--omg .panel { left: 14px; top: 22px; width: 148px; height: 176px; background: var(--paper); border: 1px solid var(--ink); }
  .label--omg .panel::before { content: ""; position: absolute; inset: 4px; border: 1px solid var(--ink); }
  .label--omg .hand-art { left: 56px; top: 34px; width: 64px; height: 62px; border-radius: 10px;
    background: linear-gradient(#f3f3f3, #d8d8d8); }
  .label--omg .word-omg { left: 0; right: 0; top: 100px; text-align: center; font-size: 40px; line-height: 1; }
  .label--omg .tagline { left: 0; right: 0; top: 150px; text-align: center; font-size: 8px; line-height: 1.3; }
</style>
</head>
<body>
<main class="label-set">

  <section class="label label--real" aria-label="Shit just got real">
    <div class="abs badge"></div>
    <p class="abs script-brush word-shit">Shit</p>
    <p class="abs caps word-got">Just got</p>
    <div class="abs ring-art" role="img" aria-label="Small diamond ring illustration"></div>
    <p class="abs script-brush word-real">real</p>
  </section>

  <section class="label label--yeah" aria-label="Ah yeah, he put a ring on it">
    <svg class="abs heart" viewBox="0 0 100 90" role="img" aria-label="Gold heart with a hand wearing a ring">
      <defs><linearGradient id="goldHeart" x1="0" y1="0" x2="1" y2="1"><stop offset="0" stop-color="#e6cd8a"/><stop offset=".5" stop-color="#b8913f"/><stop offset="1" stop-color="#d8bd74"/></linearGradient></defs>
      <path d="M50 88 C20 65 2 48 2 26 C2 12 13 2 26 2 C37 2 45 9 50 18 C55 9 63 2 74 2 C87 2 98 12 98 26 C98 48 80 65 50 88 Z" fill="url(#goldHeart)"/>
    </svg>
    <p class="abs script-brush word-yeah">Ah Yeah!</p>
    <p class="abs caps tagline">He put a ring on it</p>
  </section>

  <section class="label label--holy" aria-label="Holy shit, we're getting married">
    <p class="abs script-fine word-holy">Holy<br>Shit</p>
    <div class="abs hearts-art" role="img" aria-label="Cluster of gold, white and black hearts"></div>
    <div class="abs gold-band"></div>
    <div class="abs dark-band caps"><p>We're getting<br>married</p></div>
  </section>

  <section class="label label--mrs" aria-label="Mr and Mrs">
    <svg class="abs heart" viewBox="0 0 100 90" aria-hidden="true">
      <path d="M50 88 C20 65 2 48 2 26 C2 12 13 2 26 2 C37 2 45 9 50 18 C55 9 63 2 74 2 C87 2 98 12 98 26 C98 48 80 65 50 88 Z" fill="#ffffff"/>
    </svg>
    <p class="abs script-fine word-mrs">Mr&amp;Mrs</p>
  </section>

  <section class="label label--finally" aria-label="Fucking finally">
    <div class="abs confetti confetti--top" role="img" aria-label="Pink, gold and black confetti dots"></div>
    <div class="abs hand-art" role="img" aria-label="Line drawing of a hand showing an engagement ring"></div>
    <p class="abs script-fine word-finally">Fucking<br>finally</p>
    <div class="abs confetti confetti--bottom" role="img" aria-label="Pink, gold and black confetti dots"></div>
  </section>

  <section class="label label--omg" aria-label="OMG you're getting married">
    <div class="abs panel"></div>
    <div class="abs hand-art" role="img" aria-label="Line drawing of a hand holding a diamond ring"></div>
    <p class="abs script-brush word-omg">OMG</p>
    <p class="abs caps tagline">You're<br>getting married</p>
  </section>

</main>
</body>
</html>
```